Business card for pediatric occupational therapist

I need a business card design for my independent occupational therapy company. I am a pediatric occupational therapist working with children 0-3 years of age. I would like the card to be clean (not too 'busy') and can include pictures/cartoon-like images of children, or toys such as building blocks, or other images that would be relevant to pediatric therapy. I want it to look professional but also intended to be clear that services provided are for children.
Target Market(s)
Families requiring occupational therapy services for their children (physical, emotional, social needs) - developmental delays
Industry/Entity Type
Rehabilitation
Contact Information for Business Card
Marisa Dunphrey OT LLC
Marisa Dunphrey, OTR/L
Occupational Therapist
marisa.dunphreyOT@brightmail.example

```html
<!DOCTYPE html>
<html lang="en">
<head>
<meta charset="utf-8">
<title>Marisa Dunphrey – Occupational Therapist Business Card</title>
<link href="https://fonts.googleapis.com/css2?family=Caveat+Brush&family=Patrick+Hand&family=Mulish:wght@700&display=swap" rel="stylesheet">
<style>
  :root {
    --periwinkle: #6574b3;
    --periwinkle-soft: #95a3d0;
    --lavender-tab: #c3cae6;
    --paper: #ffffff;
    --board: #f7f8fc;
    --doodle-tint: #e9ecf7;
    --ink: #111111;
    --ink-soft: #333333;
  }
  * { margin: 0; padding: 0; box-sizing: border-box; }
  html, body { width: 1200px; height: 1200px; overflow: hidden; }
  body { background: var(--board); position: relative; font-family: "Mulish", sans-serif; }

  .board-pattern {
    position: absolute; inset: 0;
    background: radial-gradient(circle at 30% 30%, var(--doodle-tint) 0%, var(--board) 55%),
                radial-gradient(circle at 75% 75%, var(--doodle-tint) 0%, transparent 50%);
  }

  .side-bar {
    position: absolute; top: 107px; width: 68px; height: 247px;
    background: var(--periwinkle);
  }
  .side-bar--left { left: 0; border-radius: 0 18px 18px 0; }
  .side-bar--right { right: 0; border-radius: 18px 0 0 18px; }

  .brand-heading {
    position: absolute; top: 140px; left: 0; width: 1200px; text-align: center;
  }
  .brand-name {
    font-family: "Caveat Brush", cursive; font-weight: 400;
    font-size: 124px; line-height: 1; color: var(--periwinkle);
  }
  .brand-role {
    font-family: "Patrick Hand", cursive; font-weight: 400; font-size: 52px; line-height: 1;
    color: var(--ink); margin-top: 12px;
  }

  .card {
    position: absolute; top: 498px; width: 441px; height: 252px;
    box-shadow: 10px 10px 10px rgba(0,0,0,0.45);
    overflow: hidden;
  }
  .card--front { left: 134px; background: var(--paper); }
  .card--back { left: 625px; background: var(--periwinkle-soft); }

  .card-pattern { position: absolute; inset: 0; }
  .card--front .card-pattern { background: linear-gradient(135deg, #fbfbfe, #f1f3fa); }
  .card--back .card-pattern { background: linear-gradient(135deg, #9aa7d3, #8e9ccb); }

  .card-tab { position: absolute; top: 58px; width: 23px; height: 136px; }
  .card-tab--left { left: 0; border-radius: 0 6px 6px 0; }
  .card-tab--right { right: 0; border-radius: 6px 0 0 6px; }
  .card--front .card-tab { background: var(--lavender-tab); }
  .card--back .card-tab { background: var(--periwinkle); }

  .card-name {
    position: absolute; left: 0; width: 100%; text-align: center;
    font-family: "Caveat Brush", cursive; font-weight: 400; font-size: 48px; line-height: 1;
  }
  .card-role {
    position: absolute; left: 0; width: 100%; text-align: center;
    font-family: "Patrick Hand", cursive; font-weight: 400; font-size: 21px; line-height: 1;
  }
  .card--front .card-name { top: 86px; color: var(--periwinkle); }
  .card--front .card-role { top: 136px; color: var(--ink-soft); }
  .card--back .card-name { top: 88px; color: var(--paper); }
  .card--back .card-role { top: 140px; color: var(--paper); }

  .contact-list { position: absolute; left: 112px; top: 174px; list-style: none; }
  .contact-item {
    display: flex; align-items: center; gap: 7px;
    font-size: 13px; font-weight: 700; color: var(--periwinkle); line-height: 19.5px;
    white-space: nowrap;
  }
  .contact-item--company { padding-left: 21px; }
  .contact-icon { width: 14px; height: 14px; flex: none; }
</style>
</head>
<body>
  <div class="board-pattern" role="img" aria-label="Soft repeating pattern of hand-drawn toys: blocks, trains, cars, bicycles, stars and hearts"></div>

  <div class="side-bar side-bar--left"></div>
  <div class="side-bar side-bar--right"></div>

  <header class="brand-heading">
    <h1 class="brand-name">Marisa Dunphrey</h1>
    <p class="brand-role">Occupational Therapist</p>
  </header>

  <section class="card card--front">
    <div class="card-pattern" role="img" aria-label="Light doodle pattern of children's toys"></div>
    <div class="card-tab card-tab--left"></div>
    <div class="card-tab card-tab--right"></div>
    <h2 class="card-name">Marisa Dunphrey</h2>
    <p class="card-role">Occupational Therapist</p>
    <ul class="contact-list">
      <li class="contact-item contact-item--company">Marisa Dunphrey OT LLC</li>
      <li class="contact-item">
        <svg class="contact-icon" viewBox="0 0 14 14" aria-hidden="true">
          <rect width="14" height="14" rx="3" fill="#6574b3"/>
          <path d="M4.3 3.2 5.8 4.9 5 6a5 5 0 0 0 3 3l1.1-.8 1.7 1.5-.9 1.1C7 10.6 3.4 7 3.2 4.1z" fill="#fff"/>
        </svg>
        0000.5550.1426
      </li>
      <li class="contact-item">
        <svg class="contact-icon" viewBox="0 0 14 14" aria-hidden="true">
          <rect width="14" height="14" rx="3" fill="#6574b3"/>
          <rect x="3" y="4.2" width="8" height="5.6" fill="none" stroke="#fff" stroke-width="1"/>
          <path d="M3 4.2 7 7.4 11 4.2M3 9.8l3-2.6M11 9.8 8 7.2" fill="none" stroke="#fff" stroke-width="0.9"/>
        </svg>
        marisa.dunphreyOT@brightmail.example
      </li>
    </ul>
  </section>

  <section class="card card--back">
    <div class="card-pattern" role="img" aria-label="Doodle pattern of children's toys on periwinkle"></div>
    <div class="card-tab card-tab--left"></div>
    <div class="card-tab card-tab--right"></div>
    <h2 class="card-name">Marisa Dunphrey</h2>
    <p class="card-role">Occupational Therapist</p>
  </section>
</body>
</html>
```